Label Design Refresh for existing High End Supplement line

Design a label for our high end supplement brand, packaged in a Cobal Blue bottle.... using Clear labels as the label stock media.

A clear label design will take advantage of the blue bottle and can incorporate any design element you create, metalic elements, new graphics etc.

our line spans 50 different product categories and over 400 unique SKUs, so any elements you suggest to differentiate products or categories will be appreciated.

see: www.velmorahealth.com
Updates

Need designers to meet project requirements. Full label, clear label stock design (clear background with exception for design elements and text etc.)

Target Market(s)

Men and Women 25-55 Health conscious and not price sensitive. Product is 5x higher cost than competition.

Industry/Entity Type

Sexual health for men and women. testosterone, hormone health, nootropics

Font styles to use
Sans Serif

Colors

Designer to choose colors to be used in the design.

Requirements
Must have
• Clear label design for Cobalt blue, packer style, pharma bottle. Must feature Velmora brand on front panel. Must show entire label panel design as 2.8in x 7.25in. Graphics can be full color with metalic or foil type elements.
Nice to have
• Name of products include: SHBG, Testosterone & Libido, Adrenal Support Phase 2, LH Formula, ADHD Phase1,
Should not have
• Busy designs that are stock images for supplement label layouts

```html
<!DOCTYPE html>
<html lang="en">
<head>
<meta charset="utf-8">
<title>Velmora Lung Repair Label</title>
<link rel="stylesheet" href="https://fonts.googleapis.com/css2?family=Montserrat:wght@400;500;600;700;800&display=swap">
<style>
  :root {
    --page: #eeeff1;
    --cobalt: #1a1ad8;
    --cobalt-deep: #0c0c9a;
    --cobalt-light: #3b49f0;
    --white: #ffffff;
    --lime: #d2f27a;
    --leaf: #9fd86a;
    --leaf-deep: #6fbf6a;
    --badge-grey: #c9ccd6;
    --badge-ink: #4b55b8;
  }
  * { margin: 0; padding: 0; box-sizing: border-box; }
  html, body { width: 1200px; height: 1200px; overflow: hidden; }
  body {
    background: var(--page);
    font-family: "Montserrat", sans-serif;
    color: var(--white);
    position: relative;
  }
  .label-panel {
    position: absolute;
    left: 280px; top: 100px;
    width: 640px; height: 1000px;
    border-radius: 36px;
    background: linear-gradient(100deg, var(--cobalt-deep) 0%, var(--cobalt) 30%, var(--cobalt-light) 50%, var(--cobalt) 72%, var(--cobalt-deep) 100%);
    overflow: hidden;
  }
  .brand {
    position: absolute; left: 74px; top: 96px;
    display: flex; align-items: center; gap: 12px;
    font-size: 52px; font-weight: 800; letter-spacing: -1px; line-height: 1;
  }
  .brand-dot {
    width: 26px; height: 26px; border-radius: 50%;
    background: var(--white);
  }
  .category {
    position: absolute; left: 82px; top: 172px;
    font-size: 23px; font-weight: 700; line-height: 1.4;
  }
  .category .spectrum { color: var(--lime); display: block; }
  .product-name {
    position: absolute; left: 74px; top: 250px;
    font-size: 172px; font-weight: 800; letter-spacing: -4px; line-height: 1;
  }
  .product-sub {
    position: absolute; left: 80px; top: 438px;
    font-size: 60px; font-weight: 400; line-height: 1;
  }
  .count-badge {
    position: absolute; left: 84px; top: 592px;
    width: 142px; height: 166px;
    border: 3px solid var(--badge-grey);
    border-radius: 18px 18px 4px 4px;
    text-align: center;
  }
  .count-badge .count {
    display: block; margin-top: 10px;
    font-size: 78px; font-weight: 800; line-height: 1; color: var(--lime);
  }
  .count-badge .caption {
    position: absolute; left: 0; right: 0; bottom: 0; height: 62px;
    background: linear-gradient(180deg, #ffffff, var(--badge-grey));
    color: var(--badge-ink);
    padding-top: 6px;
  }
  .caption .veggie { display: block; font-size: 24px; font-weight: 800; line-height: 1; }
  .caption .caps { display: block; font-size: 18px; font-weight: 400; line-height: 1.2; }
  .leaf-art {
    position: absolute; left: 300px; top: 470px;
    width: 300px; height: 300px; border-radius: 50%;
    background: radial-gradient(circle at 50% 50%, var(--lime) 0%, var(--leaf) 45%, var(--leaf-deep) 70%, rgba(111,191,106,0) 72%);
    opacity: 0.9;
  }
  .benefits {
    position: absolute; left: 74px; top: 818px; width: 520px;
    list-style: none;
  }
  .benefits li {
    position: relative; padding-left: 22px; margin-bottom: 10px;
    font-size: 13px; font-weight: 600; text-transform: uppercase; line-height: 1.35;
  }
  .benefits li svg { position: absolute; left: 0; top: 0; }
</style>
</head>
<body>
  <main class="label-panel">
    <div class="brand"><span class="brand-dot"></span>VELMORA</div>
    <div class="category"><span class="spectrum">FULL SPECTRUM</span>SUPPLEMENT</div>
    <h1 class="product-name">LUNG</h1>
    <div class="product-sub">Repair</div>

    <div class="count-badge">
      <span class="count">60</span>
      <div class="caption"><span class="veggie">VEGGIE</span><span class="caps">CAPSULES</span></div>
    </div>

    <div class="leaf-art" role="img" aria-label="Circular cluster of green leaves illustration"></div>

    <ul class="benefits">
      <li><svg width="14" height="14" viewBox="0 0 14 14"><path d="M1 13 C1 5 5 1 13 1 C13 9 9 13 1 13 Z" fill="#9fd86a"/></svg>Formulated with bovine lung tissue with additional nutritional factors to support lung healing and repair</li>
      <li><svg width="14" height="14" viewBox="0 0 14 14"><path d="M1 13 C1 5 5 1 13 1 C13 9 9 13 1 13 Z" fill="#9fd86a"/></svg>Reduces major symptoms as bronchial hyperactivity, mucus production and airway inflammation</li>
      <li><svg width="14" height="14" viewBox="0 0 14 14"><path d="M1 13 C1 5 5 1 13 1 C13 9 9 13 1 13 Z" fill="#9fd86a"/></svg>Combines broncho-dilating and antispasmodic actions specific for the lungs</li>
    </ul>
  </main>
</body>
</html>
```